Website Design for Forklift Training Company

DO NOT CONTACT PRIVATELY. ONLY SUBMISSIONS HERE WILL BE CONSIDERED

I need a design for a website that offers forklift training courses.

The company offers accredited, onsite forklift training that are customized for the needs of each individual company. The company offers a variety of courses to operate forklifts and other machinary.

About: "Pembrook Lift Academy Ltd delivers bespoke onsite forklift truck operator training throught the uk.
All our instructors have a wealth of knowledge and expertise to provide your company with all your forklift truck training requirements.
Pembrook Lift Academy Ltd is registered and accredited by qkmvd standards so you can be rest assured that all forklift training is carried out the very highest standard"

I need the following pages designed:
> a) Home Page: Include a header image, ways to contact, about snippet, overview of courses, accreditation that will be received after completing the courses. (See attachments for samples)
> b) About Page
> c) Contact Us Page
> d) Course Page Template: A page that will be used as template for the courses offered. It should contain;
1. Cover image for the course
2. A description of the course
3. A table indicating the various course options
4. Course Objectives
5. What the trainee will receive after doing the course (example: a certification)

Target Market(s)

Industrial Businesses

Number of Pages Required

4 page

Colors
0054AA
0677BA
7BADD7
CADEEF
E8F1F8
0094D4
00A9DD
6FCCEA
C7EBF8
E9F6FB

Requirements
Should not have
• - No Search bar

```html
<!DOCTYPE html>
<html lang="en">
<head>
<meta charset="utf-8">
<title>Pembrook Lift Academy Ltd – Forklift Training</title>
<link href="https://fonts.googleapis.com/css2?family=Poppins:wght@400;500;600;700&display=swap" rel="stylesheet">
<style>
:root{
  --blue-deep:#0054AA;
  --blue-mid:#0677BA;
  --blue-soft:#7BADD7;
  --blue-pale:#CADEEF;
  --blue-mist:#E8F1F8;
  --cyan-deep:#0094D4;
  --cyan:#00A9DD;
  --cyan-soft:#6FCCEA;
  --cyan-pale:#C7EBF8;
  --cyan-mist:#E9F6FB;
  --navy:#0c2346;
  --ink:#1b1b1b;
  --white:#ffffff;
}
*{box-sizing:border-box;margin:0;padding:0}
html,body{width:1200px;height:2870px;overflow:hidden}
body{position:relative;background:var(--white);font-family:'Poppins',sans-serif;color:var(--ink)}
.abs{position:absolute}
.btn{position:absolute;display:flex;align-items:center;justify-content:center;border-radius:20px;font-weight:500;font-size:15px}
.btn-solid{background:var(--blue-deep);color:var(--white);font-weight:600}
.btn-ghost{border:2px solid #cfcfcf;color:var(--ink);background:var(--white)}

/* header */
.site-header{position:absolute;left:0;top:0;width:1200px;height:77px;background:var(--white)}
.brand{position:absolute;display:flex;align-items:center;gap:10px}
.brand-mark{width:22px;height:22px;background:var(--cyan-deep)}
.brand-name{font-size:20px;font-weight:600;color:var(--cyan-deep);white-space:nowrap}
.main-nav a{position:absolute;top:30px;font-size:13px;font-weight:500;color:var(--ink);text-decoration:none;letter-spacing:.2px}
.main-nav a.active{color:var(--cyan-deep)}
.main-nav a.active::after{content:"";position:absolute;left:0;top:20px;width:18px;height:3px;background:var(--cyan-deep)}

/* hero */
.hero-photo{position:absolute;left:0;top:77px;width:1200px;height:490px;
  background:linear-gradient(100deg,#3a3630 0%,#57503f 30%,#6b5f3a 45%,#4a4a44 65%,#5a5648 100%);
  clip-path:polygon(0 0,100% 0,100% 100%,0 93%)}
.hero-title{position:absolute;left:0;top:262px;width:1200px;text-align:center;font-size:47px;font-weight:700;color:var(--white);letter-spacing:.5px}
.swatches{position:absolute;left:430px;top:585px;display:flex}
.swatches span{width:27px;height:25px}

/* about */
.section-title{font-weight:700;color:var(--cyan-deep)}
.about-title{left:88px;top:652px;font-size:35px}
.about-copy{left:88px;top:723px;width:480px;font-size:14.5px;line-height:20px;color:#222}
.about-copy p{margin-bottom:20px}
.about-photo{left:705px;top:647px;width:407px;height:375px;border-radius:30px;
  background:linear-gradient(135deg,#e39a2a 0%,#c9a05a 35%,#6a8fbf 60%,#e0742c 100%)}
.about-badge{left:648px;top:832px;width:205px;height:165px;border-radius:24px;background:var(--white);box-shadow:0 6px 22px rgba(0,0,0,.15);display:flex;align-items:center;justify-content:center}
.about-badge div{width:138px;height:104px;border-radius:10px;background:linear-gradient(135deg,#f3c623,#8a6d4a)}

/* accreditation */
.accred{left:0;top:1111px;width:1200px;height:168px;background:var(--blue-mist)}
.accred-label{left:257px;top:1180px;font-size:25px;font-weight:600;color:var(--ink)}
.badge-a{left:706px;top:1158px;width:98px;height:60px;border-radius:8px;background:#2f3f8f}
.badge-b{left:861px;top:1145px;width:80px;height:86px;background:#1f2c73;border:3px solid #2a5fbf}

/* courses */
.courses{left:0;top:1279px;width:1200px;height:601px;background:linear-gradient(180deg,#12315f 0%,#0d2750 50%,#0b2146 100%)}
.courses-title{left:0;top:1360px;width:1200px;text-align:center;font-size:35px;font-weight:600;color:var(--white)}
.course-card{position:absolute;top:1441px;width:324px;height:355px;background:var(--white)}
.course-head{height:106px;background:var(--cyan);padding:30px 0 0 32px;color:var(--white)}
.course-head h3{font-size:25px;font-weight:600;line-height:28px}
.course-head p{font-size:19px;line-height:24px}
.course-list{list-style:none;padding:36px 20px 0 32px}
.course-list li{position:relative;padding-left:17px;font-size:14px;line-height:20px;margin-bottom:4px;color:#222}
.course-list li::before{content:"";position:absolute;left:0;top:5px;width:9px;height:9px;border:1.5px solid var(--cyan-deep);border-radius:50%}
.course-list li::after{content:"";position:absolute;left:3px;top:8.5px;width:4px;height:1.5px;background:var(--cyan-deep)}
.course-card .btn{left:32px;top:293px;width:145px;height:39px}

/* inquiry */
.inquiry{left:232px;top:1996px;width:736px;height:304px;background:var(--white);box-shadow:0 0 14px rgba(0,0,0,.08)}
.inquiry-title{left:0;top:2030px;width:1214px;text-align:center;font-size:25px;font-weight:600;color:var(--cyan-deep)}
.field{position:absolute;height:37px;border:1px solid #d9dee4;border-radius:20px;display:flex;align-items:center;gap:7px;padding-left:16px;font-size:12px;color:#777}
.field svg{width:14px;height:14px;fill:none;stroke:var(--blue-soft);stroke-width:1.6}
.field-msg{height:61px;align-items:flex-start;padding-top:11px;border-radius:14px}

/* footer */
.footer{left:0;top:2410px;width:1200px;height:420px;background:linear-gradient(180deg,#0e2b57 0%,#0a2148 100%)}
.foot-head{font-size:17px;font-weight:600;color:var(--cyan)}
.contact-item{position:absolute;display:flex;align-items:center;gap:12px;color:var(--white);font-size:13px;line-height:19px}
.contact-item .ic{width:42px;height:42px;border-radius:50%;background:var(--cyan-deep);display:flex;align-items:center;justify-content:center;flex:none}
.contact-item .ic svg{width:18px;height:18px;fill:var(--white)}
.contact-item small{display:block;font-size:13.5px;color:var(--cyan)}
.hours{left:584px;top:2628px;color:var(--white);font-size:13px}
.hours div{display:flex;height:32.5px}
.hours span:first-child{width:83px}
.map{left:863px;top:2586px;width:249px;height:143px;border-radius:6px;background:linear-gradient(135deg,#eef1f4,#dfe5ea)}
.foot-nav a{position:absolute;top:2790px;font-size:13.5px;color:var(--white);text-decoration:none}
.foot-nav a.active{color:var(--cyan);text-decoration:underline}
.bottom-bar{left:0;top:2830px;width:1200px;height:40px;background:var(--blue-mid);color:var(--white);font-size:13px}
.bottom-bar p{position:absolute;left:89px;top:11px}
.social{position:absolute;top:14px;width:12px;height:12px;border-radius:50%;background:var(--white)}
</style>
</head>
<body>

<header class="site-header">
  <div class="brand" style="left:88px;top:27px">
    <span class="brand-mark"></span><span class="brand-name">Pembrook Lift Academy Ltd</span>
  </div>
  <nav class="main-nav">
    <a class="active" href="#" style="left:579px">HOME</a>
    <a href="#" style="left:652px">ABOUT US</a>
    <a href="#" style="left:750px">COURSE</a>
    <a href="#" style="left:835px">CONTACT US</a>
  </nav>
  <a class="btn btn-solid" style="left:967px;top:21px;width:145px;height:35px">Inquire Now</a>
</header>

<div class="hero-photo" role="img" aria-label="Forklift instructor in hard hat and hi-vis vest beside a yellow forklift in a warehouse"></div>
<svg class="abs" style="left:0;top:520px" width="1200" height="60" viewBox="0 520 1200 60">
  <polygon points="0,536 690,552 0,572" fill="#0094D4"/>
</svg>
<h1 class="hero-title">FORKLIFT TRAINING</h1>
<a class="btn btn-solid" style="left:526px;top:331px;width:149px;height:35px;background:var(--cyan-deep)">Contact Us</a>

<div class="swatches">
  <span style="background:var(--blue-deep)"></span><span style="background:var(--blue-mid)"></span><span style="background:var(--blue-soft)"></span><span style="background:var(--blue-pale)"></span><span style="background:var(--blue-mist)"></span><span style="background:var(--cyan-deep)"></span><span style="background:var(--cyan)"></span><span style="background:var(--cyan-soft)"></span><span style="background:var(--cyan-pale)"></span><span style="background:var(--cyan-mist)"></span>
</div>

<h2 class="abs section-title about-title">About Us</h2>
<div class="abs about-copy">
  <p>"Pembrook Lift Academy Ltd delivers bespoke onsite forklift truck operator training throughout the UK.</p>
  <p>All our instructors have a wealth of knowledge and expertise to provide your company with all your forklift truck training requirements.</p>
  <p>Pembrook Lift Academy Ltd is registered and accredited by qkmvd standards so you can be rest assured that all forklift training is carried out the very highest standard"</p>
</div>
<a class="btn btn-ghost" style="left:88px;top:968px;width:143px;height:40px">Read More</a>
<div class="abs about-photo" role="img" aria-label="Smiling warehouse worker in blue hard hat and orange hi-vis vest"></div>
<div class="abs about-badge"><div role="img" aria-label="Forklift icon"></div></div>

<div class="abs accred"></div>
<h3 class="abs accred-label">Forklift Training Accreditation:</h3>
<div class="abs badge-a" role="img" aria-label="Workplace transport accreditation badge"></div>
<div class="abs badge-b" role="img" aria-label="qkmvd accredited badge"></div>

<div class="abs courses" role="img" aria-label="Dark blue tinted warehouse shelving"></div>
<svg class="abs" style="left:0;top:1240px" width="1200" height="50" viewBox="0 1240 1200 50">
  <polygon points="0,1276 1200,1290 1200,1292 0,1292" fill="#0f2c58"/>
  <polygon points="480,1283 1200,1248 1200,1289" fill="#0094D4"/>
</svg>
<h2 class="abs courses-title">Forklift Training Courses</h2>

<article class="course-card" style="left:88px">
  <div class="course-head"><h3>Forklift Training</h3><p>Courses</p></div>
  <ul class="course-list">
    <li>Articulated Truck Training Course</li>
    <li>Sideloader Lift Training course</li>
    <li>Counterbalance Training Course</li>
    <li>Pivot Steer Truck Training Course</li>
    <li>Lorry Loader Crane Training Course</li>
  </ul>
  <a class="btn btn-ghost">Read More</a>
</article>
<article class="course-card" style="left:438px">
  <div class="course-head"><h3>Mewp Training</h3><p>Courses</p></div>
  <ul class="course-list">
    <li>Cherry Picker Training Course</li>
    <li>Scissor Lift Training Course</li>
    <li>Harness And Lanyard Training Course</li>
  </ul>
  <a class="btn btn-ghost">Read More</a>
</article>
<article class="course-card" style="left:788px">
  <div class="course-head"><h3>Other Training</h3><p>Courses</p></div>
  <ul class="course-list">
    <li>Skid Steer Loader Training Course</li>
    <li>Front Loading Shovel Training Course</li>
    <li>Overhead Pendant Crane Training Course</li>
  </ul>
  <a class="btn btn-solid">Read More</a>
</article>

<svg class="abs" style="left:0;top:1880px" width="1200" height="50" viewBox="0 1880 1200 50">
  <polygon points="0,1883 815,1883 0,1926" fill="#0094D4"/>
</svg>

<div class="abs inquiry"></div>
<h2 class="abs inquiry-title">Quick Inquiry</h2>
<div class="field" style="left:264px;top:2092px;width:218px">
  <svg viewBox="0 0 16 16"><circle cx="8" cy="5" r="3"/><path d="M2 15c0-3.5 2.7-5 6-5s6 1.5 6 5"/></svg>Name</div>
<div class="field" style="left:491px;top:2092px;width:219px">
  <svg viewBox="0 0 16 16"><rect x="4" y="1.5" width="8" height="13" rx="1.5"/></svg>Phone</div>
<div class="field" style="left:720px;top:2092px;width:218px">
  <svg viewBox="0 0 16 16"><rect x="1.5" y="3.5" width="13" height="9" rx="1"/><path d="M1.5 4l6.5 5 6.5-5"/></svg>Email</div>
<div class="field field-msg" style="left:264px;top:2145px;width:674px">
  <svg viewBox="0 0 16 16"><path d="M2 2h12v8l-4 4H2z"/><path d="M10 14v-4h4"/></svg>Message</div>
<a class="btn btn-solid" style="left:546px;top:2231px;width:122px;height:35px">Submit</a>

<div class="abs footer" role="img" aria-label="Dark blue tinted forklift background"></div>
<svg class="abs" style="left:0;top:2365px" width="1200" height="60" viewBox="0 2365 1200 60">
  <polygon points="520,2410 1200,2371 1200,2420" fill="#0094D4"/>
</svg>
<div class="brand" style="left:468px;top:2457px">
  <span class="brand-mark"></span><span class="brand-name" style="color:var(--white)">Pembrook Lift Academy Ltd</span>
</div>

<h4 class="abs foot-head" style="left:88px;top:2581px">Conatct info</h4>
<div class="contact-item" style="left:88px;top:2619px">
  <span class="ic"><svg viewBox="0 0 24 24"><path d="M12 2a7 7 0 0 0-7 7c0 5 7 13 7 13s7-8 7-13a7 7 0 0 0-7-7zm0 9.5A2.5 2.5 0 1 1 12 6.5a2.5 2.5 0 0 1 0 5z"/></svg></span>
  <span>14 Harlow Yard, Brentmere,<br>Ashcombe, AB12 3CD</span>
</div>
<div class="contact-item" style="left:353px;top:2619px">
  <span class="ic"><svg viewBox="0 0 24 24"><path d="M6.6 10.8a15 15 0 0 0 6.6 6.6l2.2-2.2a1 1 0 0 1 1-.25 11.4 11.4 0 0 0 3.6.57 1 1 0 0 1 1 1V20a1 1 0 0 1-1 1A17 17 0 0 1 3 4a1 1 0 0 1 1-1h3.5a1 1 0 0 1 1 1c0 1.250.2 2.450.57 3.570a1 1 0 0 1-.25 1z"/></svg></span>
  <span><small>Phone</small>07700 900418</span>
</div>
<div class="contact-item" style="left:88px;top:2684px">
  <span class="ic"><svg viewBox="0 0 24 24"><path d="M3 5h18v14H3z M3 5l9 7 9-7" fill="none" stroke="#fff" stroke-width="2"/></svg></span>
  <span><small>Email</small>info@pembrook-lift.co.uk</span>
</div>
<div class="contact-item" style="left:353px;top:2684px">
  <span class="ic"><svg viewBox="0 0 24 24"><path d="M7 3h10v5H7z M4 9h16v8h-3v4H7v-4H4z M9 15v4h6v-4z"/></svg></span>
  <span><small>Telephone/Fax</small>01632 960274</span>
</div>

<h4 class="abs foot-head" style="left:584px;top:2581px">Business Hours</h4>
<div class="abs hours">
  <div><span>Mon - Fri</span><span>Open 24 Hours</span></div>
  <div><span>Saturday</span><span>6:00 - 18:00</span></div>
  <div><span>Sunday</span><span>Appointment Only</span></div>
</div>
<div class="abs map" role="img" aria-label="Street map showing the training centre location"></div>

<nav class="foot-nav">
  <a class="active" href="#" style="left:420px">Home</a>
  <a href="#" style="left:507px">About Us</a>
  <a href="#" style="left:614px">Course</a>
  <a href="#" style="left:705px">Contact Us</a>
</nav>

<footer class="abs bottom-bar">
  <p>Copyright © 2021 Pembrook Lift Academy Ltd. All Rights Reserved</p>
  <span class="social" style="left:1003px"></span>
  <span class="social" style="left:1033px"></span>
  <span class="social" style="left:1066px"></span>
  <span class="social" style="left:1099px"></span>
</footer>

</body>
</html>
```